Mediation service showing compassion, collaboration, and resolution

I would like to purchase a customized version of a design you have previously submitted - https://www.brieflyart.example/design/48172036

Hello,

I would like a design for a flyer for my mediation business.
I also want to include a message that says that I offer rates on sliding scale.
My website is: www.morvenpeaceadr.example

Let me know what other details you might want?

Thank you,

Tobias

Target Market(s)

Local community, western Massachusetts USA. Businesses, families, individuals.

Industry/Entity Type

Mediation, Legal, Alternative Dispute Resolution, Divorce, Unions

Font styles to use
Sans Serif

Colors
0094D4
00A9DD
6FCCEA
C7EBF8
E9F6FB
00AB8E
00BBA5
67D7C9
C6EFE9
E9F9F6

Requirements
Must have
• “Sliding scale rates available “. Phone and email details. +1.555.784.3091 and email: tobias@morvenpeaceadr.example as well as we code to my website www.morvenpeaceadr.example

```html
<!DOCTYPE html>
<html lang="en">
<head>
<meta charset="utf-8">
<title>Tobias F. Morven – Mediation Flyer</title>
<link href="https://fonts.googleapis.com/css2?family=Cormorant+Garamond:wght@400;500;600;700&display=swap" rel="stylesheet">
<style>
  :root {
    --blue-deep: #0094D4;
    --blue: #00A9DD;
    --blue-soft: #6FCCEA;
    --blue-pale: #C7EBF8;
    --blue-mist: #E9F6FB;
    --teal: #00BBA5;
    --teal-soft: #67D7C9;
    --ink: #111111;
    --text: #2b2b2b;
    --paper: #fdfdfe;
    --white: #ffffff;
  }
  * { margin: 0; padding: 0; box-sizing: border-box; }
  html, body { width: 982px; height: 1200px; overflow: hidden; background: var(--paper); }
  body { font-family: "Cormorant Garamond", Georgia, serif; color: var(--text); }

  .flyer { position: relative; width: 982px; height: 1200px; overflow: hidden; background: var(--paper); }

  .hero-photo {
    position: absolute; left: 520px; top: 0; width: 462px; height: 430px;
    background: linear-gradient(90deg, rgba(253,253,254,1) 0%, rgba(225,235,246,1) 20%, rgba(200,217,235,1) 55%, rgba(190,208,230,1) 80%, rgba(212,227,241,1) 100%);
  }

  .backdrop { position: absolute; left: 0; top: 0; }

  .brand { position: absolute; text-align: center; color: var(--ink); }
  .brand-name { display: block; font-weight: 500; font-size: 40px; line-height: 1; letter-spacing: 0.5px; }
  .brand-tag { display: block; font-weight: 600; font-size: 12.5px; letter-spacing: 0.6px; margin-top: 10px; }
  .brand--top { left: 51px; top: 40px; width: 420px; }
  .brand--bottom { left: 29px; top: 1014px; width: 390px; }
  .brand--bottom .brand-name { font-size: 38px; }

  .title-box {
    position: absolute; left: 49px; top: 197px; width: 440px; height: 67px;
    background: var(--blue-mist);
    display: flex; align-items: center; padding-left: 8px;
  }
  .title { font-weight: 700; font-size: 58px; letter-spacing: 6px; color: var(--ink); line-height: 1; }

  .intro, .role {
    position: absolute; color: var(--white); font-size: 19px; line-height: 25px; font-weight: 500;
  }
  .intro { left: 51px; top: 285px; width: 462px; }
  .role { left: 536px; top: 428px; width: 412px; }

  .art { position: absolute; }
  .art--figures { left: 536px; top: 282px; width: 248px; height: 130px; background: linear-gradient(180deg, rgba(233,246,251,0.5), rgba(199,235,248,0.3)); border-radius: 4px; }
  .art--puzzle { left: 54px; top: 430px; width: 381px; height: 190px; background: linear-gradient(135deg, rgba(233,246,251,0.55), rgba(199,235,248,0.6)); border-radius: 4px; }

  .services-heading {
    position: absolute; left: 49px; top: 652px;
    font-weight: 700; font-size: 48px; letter-spacing: 2.5px; color: var(--ink); line-height: 1;
  }
  .services-heading .accent { color: var(--blue); font-weight: 600; }

  .service-list { position: absolute; list-style: none; font-size: 20px; line-height: 22px; color: var(--text); font-weight: 500; }
  .service-list--left { left: 51px; top: 720px; width: 480px; }
  .service-list--right { left: 562px; top: 720px; width: 400px; }
  .service-list li { position: relative; padding-left: 18px; margin-bottom: 15px; }
  .tick { position: absolute; left: 0; top: 6px; width: 11px; height: 10px; }

  .rates-band { position: absolute; left: 438px; top: 1009px; width: 544px; height: 88px; }
  .rates-text {
    position: absolute; left: 499px; top: 1009px; height: 88px; width: 480px;
    display: flex; align-items: center;
    color: var(--white); font-weight: 600; font-size: 25px; letter-spacing: 0.6px;
  }

  .contact {
    position: absolute; left: 51px; top: 1133px; width: 900px;
    display: flex; align-items: center; font-size: 22px; color: var(--ink); font-weight: 500;
  }
  .contact-item { display: flex; align-items: center; gap: 9px; }
  .contact-icon { width: 18px; height: 18px; flex: none; }
  .contact-sep { margin: 0 18px; color: var(--ink); }
</style>
</head>
<body>
<main class="flyer">

  <div class="hero-photo" role="img" aria-label="Photo of business people shaking hands and applauding in a bright office"></div>

  <svg class="backdrop" width="982" height="1200" viewBox="0 0 982 1200" aria-hidden="true">
    <defs>
      <linearGradient id="bandFill" x1="0" y1="0" x2="1" y2="0.3">
        <stop offset="0" stop-color="#0094D4"/>
        <stop offset="0.5" stop-color="#00A9DD"/>
        <stop offset="1" stop-color="#5EC6D2"/>
      </linearGradient>
      <linearGradient id="lowerFill" x1="0" y1="0" x2="1" y2="1">
        <stop offset="0" stop-color="#6FCCEA"/>
        <stop offset="0.6" stop-color="#3DB6E0"/>
        <stop offset="1" stop-color="#00A9DD"/>
      </linearGradient>
    </defs>
    <polygon points="0,138 982,407 982,718 0,452" fill="url(#bandFill)" opacity="0.94"/>
    <polygon points="185,480 982,500 982,718 560,590" fill="url(#lowerFill)" opacity="0.55"/>
  </svg>

  <div class="brand brand--top">
    <span class="brand-name">Tobias F. Morven</span>
    <span class="brand-tag">Alternative Dispute Resolution</span>
  </div>

  <div class="title-box"><h1 class="title">MEDIATION</h1></div>

  <p class="intro">Mediation is a form of facilitated negotiation, by a mediator, who helps the parties engage in a dialog to search for a joint agreement. All decisions, from agreeing to participate in the mediation, to possible terms of an agreement, are decided by the parties.</p>

  <div class="art art--figures" role="img" aria-label="Line illustration of three figures holding hands raised together"></div>

  <p class="role">The mediator has no authority over the parties nor impose any directives. The mediator is there to help the parties find their interests, list and organize the options they have vs the alternatives and the outcome probabilities for each outside a resolution via the mediation process.</p>

  <div class="art art--puzzle" role="img" aria-label="Line illustration of a hand fitting puzzle pieces together with arrows"></div>

  <h2 class="services-heading"><span class="accent">SERVICES</span> PROVIDED</h2>

  <ul class="service-list service-list--left">
    <li><svg class="tick" viewBox="0 0 11 10"><path d="M1 5.5 L4 8.5 L10 1" fill="none" stroke="#00BBA5" stroke-width="1.6"/></svg>Divorce and Family Mediation</li>
    <li><svg class="tick" viewBox="0 0 11 10"><path d="M1 5.5 L4 8.5 L10 1" fill="none" stroke="#00BBA5" stroke-width="1.6"/></svg>Commercial and business related Mediation</li>
    <li><svg class="tick" viewBox="0 0 11 10"><path d="M1 5.5 L4 8.5 L10 1" fill="none" stroke="#00BBA5" stroke-width="1.6"/></svg>International business and trading conflict mediation</li>
    <li><svg class="tick" viewBox="0 0 11 10"><path d="M1 5.5 L4 8.5 L10 1" fill="none" stroke="#00BBA5" stroke-width="1.6"/></svg>Merger Negotiations &amp; Business Collaboration</li>
    <li><svg class="tick" viewBox="0 0 11 10"><path d="M1 5.5 L4 8.5 L10 1" fill="none" stroke="#00BBA5" stroke-width="1.6"/></svg>Mediation between dealer, agent, distributor and<br>supplier, manufacturer</li>
    <li><svg class="tick" viewBox="0 0 11 10"><path d="M1 5.5 L4 8.5 L10 1" fill="none" stroke="#00BBA5" stroke-width="1.6"/></svg>Contract negotiation consultancy</li>
  </ul>

  <ul class="service-list service-list--right">
    <li><svg class="tick" viewBox="0 0 11 10"><path d="M1 5.5 L4 8.5 L10 1" fill="none" stroke="#00BBA5" stroke-width="1.6"/></svg>Employment contract negotiations</li>
    <li><svg class="tick" viewBox="0 0 11 10"><path d="M1 5.5 L4 8.5 L10 1" fill="none" stroke="#00BBA5" stroke-width="1.6"/></svg>Mediation for property or entity division</li>
    <li><svg class="tick" viewBox="0 0 11 10"><path d="M1 5.5 L4 8.5 L10 1" fill="none" stroke="#00BBA5" stroke-width="1.6"/></svg>Workplace Mediation</li>
    <li><svg class="tick" viewBox="0 0 11 10"><path d="M1 5.5 L4 8.5 L10 1" fill="none" stroke="#00BBA5" stroke-width="1.6"/></svg>Mediation Coaching</li>
    <li><svg class="tick" viewBox="0 0 11 10"><path d="M1 5.5 L4 8.5 L10 1" fill="none" stroke="#00BBA5" stroke-width="1.6"/></svg>Ombuds contracting</li>
    <li><svg class="tick" viewBox="0 0 11 10"><path d="M1 5.5 L4 8.5 L10 1" fill="none" stroke="#00BBA5" stroke-width="1.6"/></svg>Mediation via videoconference</li>
    <li><svg class="tick" viewBox="0 0 11 10"><path d="M1 5.5 L4 8.5 L10 1" fill="none" stroke="#00BBA5" stroke-width="1.6"/></svg>Meetings Facilitation</li>
  </ul>

  <div class="brand brand--bottom">
    <span class="brand-name">Tobias F. Morven</span>
    <span class="brand-tag">Alternative Dispute Resolution</span>
  </div>

  <svg class="rates-band" viewBox="0 0 544 88" aria-hidden="true">
    <defs>
      <linearGradient id="ratesFill" x1="0" y1="0" x2="1" y2="0">
        <stop offset="0" stop-color="#00A9DD"/>
        <stop offset="0.6" stop-color="#2FB5DE"/>
        <stop offset="1" stop-color="#67D7C9"/>
      </linearGradient>
      <linearGradient id="ratesStripe" x1="0" y1="0" x2="0" y2="1">
        <stop offset="0" stop-color="#00A9DD"/>
        <stop offset="1" stop-color="#C7EBF8"/>
      </linearGradient>
    </defs>
    <polygon points="0,0 6,0 40,88 34,88" fill="url(#ratesStripe)"/>
    <polygon points="16,0 544,0 544,88 50,88" fill="url(#ratesFill)"/>
  </svg>
  <p class="rates-text">SLIDING SCALE RATES AVAILABLE</p>

  <div class="contact">
    <span class="contact-item">
      <svg class="contact-icon" viewBox="0 0 24 24"><path d="M6.6 10.8a15.5 15.5 0 0 0 6.6 6.6l2.2-2.2c.3-.3.7-.4 1-.2 1.1.4 2.3.6 3.6.6.6 0 1 .4 1 1V20c0 .6-.4 1-1 1A17 17 0 0 1 3 4c0-.6.4-1 1-1h3.5c.6 0 1 .4 1 1 0 1.3.2 2.5.6 3.6.1.3 0 .7-.2 1z" fill="#00A9DD"/></svg>
      +1.555.784.3091
    </span>
    <span class="contact-sep">|</span>
    <span class="contact-item">
      <svg class="contact-icon" viewBox="0 0 24 24"><rect x="2" y="5" width="20" height="14" rx="1.5" fill="#00A9DD"/><path d="M3 6.5 L12 13 L21 6.5" fill="none" stroke="#fff" stroke-width="1.8"/></svg>
      tobias@morvenpeaceadr.example
    </span>
    <span class="contact-sep">|</span>
    <span class="contact-item">
      <svg class="contact-icon" viewBox="0 0 24 24" fill="none" stroke="#00A9DD" stroke-width="1.8"><circle cx="12" cy="12" r="9.5"/><ellipse cx="12" cy="12" rx="4" ry="9.5"/><path d="M2.5 12h19M4 7h16M4 17h16"/></svg>
      www.morvenpeaceadr.example
    </span>
  </div>

</main>
</body>
</html>
```